GLA

Please send us some options for letterhead I attached our Logo. In addition to the Logo we need this information somewhere on the page

48 Harlow Lane
Cedar Falls, RI 06417
555-274-9160

```html
<!DOCTYPE html>
<html lang="en">
<head>
<meta charset="utf-8">
<title>GLA Letterhead</title>
<link rel="stylesheet" href="https://fonts.googleapis.com/css2?family=Source+Sans+3:wght@400;700&display=swap">
<style>
  :root {
    --paper: #ffffff;
    --ink: #2b2b2b;
    --brand-dark: #4b4142;
    --brand-blue: #0a80c6;
    --rule: #8a8a8a;
  }
  html, body {
    margin: 0;
    padding: 0;
    width: 985px;
    height: 1200px;
    overflow: hidden;
    background: var(--paper);
  }
  .letterhead {
    position: relative;
    width: 985px;
    height: 1200px;
    background: var(--paper);
    font-family: "Source Sans 3", Arial, sans-serif;
    color: var(--ink);
    overflow: hidden;
  }
  .brand {
    position: absolute;
    left: 40px;
    top: 52px;
    display: flex;
    align-items: center;
    gap: 22px;
  }
  .brand-mark {
    width: 96px;
    height: 96px;
    background: var(--brand-blue);
  }
  .brand-name {
    font-weight: 700;
    font-size: 92px;
    line-height: 1;
    color: var(--brand-dark);
    letter-spacing: 2px;
  }
  .address {
    position: absolute;
    left: 743px;
    top: 56px;
    padding-left: 15px;
    border-left: 1.5px solid var(--rule);
    font-size: 20px;
    line-height: 27px;
    font-weight: 400;
    font-style: normal;
  }
  .footer-rule {
    position: absolute;
    left: 0;
    bottom: 104px;
    width: 985px;
    height: 8px;
    background: var(--brand-dark);
  }
  .footer-band {
    position: absolute;
    left: 0;
    bottom: 0;
    width: 985px;
    height: 96px;
    background: var(--brand-blue);
  }
  .phone {
    position: absolute;
    right: 58px;
    bottom: 34px;
    display: flex;
    align-items: center;
    gap: 8px;
    color: var(--paper);
    font-size: 23px;
    line-height: 1;
  }
  .phone-icon {
    width: 18px;
    height: 18px;
  }
</style>
</head>
<body>
  <main class="letterhead">
    <header class="brand">
      <div class="brand-mark"></div>
      <div class="brand-name">GLA</div>
    </header>

    <address class="address">
      <div>48 Harlow Lane</div>
      <div>Cedar Falls, RI 06417</div>
    </address>

    <div class="footer-rule"></div>
    <footer class="footer-band">
      <div class="phone">
        <svg class="phone-icon" viewBox="0 0 24 24" aria-hidden="true">
          <path fill="none" stroke="currentColor" stroke-width="2" d="M6.6 2.5 L9.4 6.6 L7.6 9 C 8.8 11.8 11.6 14.9 14.8 16.4 L17.2 14.6 L21.4 17.4 L19.6 21.2 C 11.5 21 3 12.5 2.8 4.4 Z"/>
        </svg>
        <span>555-274-9160</span>
      </div>
    </footer>
  </main>
</body>
</html>
```